automatic Real Estate Sales Brochure

Print-out of 3 to 8 pages automatically on a color inkjet printer. Page size A4
All details for my Real Estate Sales Design Project are in attached file.
Here some points:
We have abound 100 real estate objects for sale (houses, flats and pieces of land).
For each item, our system creates automatically a sales documentation, which we print out and hand to the potential buyers after they've visited the object or send it by mail upon request in form of a pdf.
This document should be of 3 to maximum 8 pages.
It should be of a modern design and invite the client to read it.
The information should be clear and quick to find.
If the global look could somehow relate to the look of our web site www.velorancasa.ch, that would be nice.
The company data is there for legal reasons, but it is the agent's phone and mail that the clients should use for contact.
The photos should be of big size (2 by page?) without being distorted nor cut.
Optionally, to save ink and pages, maybe only the first 3-4 photos full size and the rest smaller?

Target Market(s)

will be printed or sent as PDF "on the fly", meaning no pre-printing at a print shop!

Industry/Entity Type

Real Estate

Font styles to use
Sans Serif

Requirements
Must have
• see details in attached file
Should not have
• no edge-to-edge printing
• no double-page printing (A3)

```html
<!DOCTYPE html>
<html lang="fr">
<head>
<meta charset="utf-8">
<title>Brochure de vente – velorancasa</title>
<link rel="stylesheet" href="https://fonts.googleapis.com/css2?family=Lato:wght@400;700;900&family=Russo+One&display=swap">
<style>
  :root{
    --brand-red:#e9525c;
    --label-red:#e2414b;
    --ink:#333;
    --page:#fff;
    --stage:#dcdcdc;
    --cell:#9b9b9b;
    --table-bg:#e6e6e6;
    --rule:#e4e4e4;
    --interior-top:#f3efe6;
    --interior-floor:#c9752f;
  }
  *{box-sizing:border-box;margin:0;padding:0}
  html,body{width:1200px;height:1200px;overflow:hidden}
  body{background:var(--stage);font-family:'Lato',sans-serif;color:var(--ink);position:relative}

  .page{position:absolute;width:391px;height:560px;background:var(--page);overflow:hidden;box-shadow:0 2px 6px rgba(0,0,0,.18)}
  .p1{left:195px;top:29px}.p2{left:614px;top:29px}
  .p3{left:195px;top:611px}.p4{left:614px;top:611px}

  .brand{position:absolute;left:0;right:0;text-align:center;font-family:'Lato',sans-serif;font-weight:900;color:var(--brand-red);letter-spacing:.5px}
  .p1 .brand{top:14px;font-size:34px}
  .p2 .brand,.p3 .brand,.p4 .brand{top:17px;font-size:22px}
  .head-rule{position:absolute;left:0;right:0;top:59px;height:1px;background:var(--rule)}

  .photo{position:absolute}
  .interior{background:linear-gradient(180deg,var(--interior-top) 0%,#eee7da 55%,#d98a40 70%,var(--interior-floor) 100%)}
  .kitchen{background:linear-gradient(180deg,#f4f1ea 0%,#e9e6df 55%,#e8e3da 72%,#cf8a48 100%)}
  .bath{background:linear-gradient(180deg,#f2f3f4 0%,#e5e8ea 60%,#d4d8dc 100%)}
  .garden{background:linear-gradient(180deg,#dbe8f0 0%,#9cc27a 40%,#4f8a34 75%,#3a6d27 100%)}
  .wardrobe{background:linear-gradient(90deg,#f5e9c8 0%,#f1e2bd 45%,#3a3430 55%,#2b2623 100%)}

  /* page 1 */
  .hero{left:0;top:70px;width:391px;height:248px;background:linear-gradient(180deg,#b9cf9a 0%,#8fae6a 30%,#c9c2ae 55%,#e3d6bf 75%,#d8c6a8 100%)}
  .title-band{position:absolute;left:0;top:318px;width:391px;height:101px;background:var(--brand-red);color:#fff;text-align:center}
  .title-band .t1{font-family:'Russo One',sans-serif;font-size:13px;margin-top:23px;letter-spacing:.3px}
  .title-band .t2{font-family:'Russo One',sans-serif;font-size:21px;margin-top:4px;letter-spacing:.5px}
  .title-band .broker{font-size:11.5px;margin-top:10px;display:flex;justify-content:center;align-items:center;gap:7px}
  .title-band .broker svg{width:9px;height:9px}
  .facts{position:absolute;left:0;top:419px;width:391px;height:96px;background:var(--table-bg)}
  .facts-grid{position:absolute;left:23px;top:24px;display:grid;grid-template-columns:93px 69px 93px 70px;column-gap:9px;row-gap:3.5px}
  .facts-grid span{height:10px;background:var(--cell);color:#fff;font-size:5.6px;line-height:10px;padding-left:4px;white-space:nowrap;overflow:hidden}
  .facts-grid .val{background:#8a8a8a}

  /* footer */
  .footer{position:absolute;left:0;top:515px;width:391px;height:29px;background:var(--brand-red);color:#fff;font-size:6.3px}
  .footer::after{content:"";position:absolute;left:0;right:0;top:29px;height:16px;background:#ededed}
  .f-col{position:absolute;top:6px;line-height:10.5px}
  .f-company{left:23px}.f-web{left:172px}.f-phone{left:312px}
  .f-col div{display:flex;align-items:center;gap:4px}
  .f-col svg{width:7px;height:7px;fill:#fff}
  .f-company .name{font-size:7px}
  .f-company .addr{padding-left:11px;font-weight:700}

  /* page 2 */
  .sec-title{position:absolute;left:23px;color:var(--label-red);font-size:11.5px;font-weight:700;letter-spacing:.3px}
  .desc{position:absolute;left:23px;top:89px;width:209px;font-size:5.2px;line-height:6.5px;text-align:justify}
  .desc p{margin-bottom:6px}
  .agent-photo{left:246px;top:90px;width:120px;height:134px;background:linear-gradient(180deg,#f2f2f2 0%,#e6e0dc 50%,#6a4a3a 100%)}
  .agent-name{position:absolute;left:246px;top:225px;width:120px;height:15px;background:var(--brand-red);color:#fff;font-size:10px;text-align:center;line-height:15px}
  .agent-phone{position:absolute;left:246px;top:244px;width:120px;text-align:center;font-size:11px;display:flex;justify-content:center;align-items:center;gap:3px}
  .agent-phone svg{width:9px;height:9px;fill:#555}
  .comm-rule{position:absolute;left:23px;top:283px;width:344px;height:1px;background:var(--rule)}
  .comm{position:absolute;top:291px;font-size:6.6px;line-height:15.3px}
  .comm b{color:var(--label-red);font-weight:400}
  .comm-left{left:23px}.comm-right{left:242px}

  .situ{position:absolute;left:23px;top:89px;width:345px;font-size:5.3px;line-height:6.6px}
</style>
</head>
<body>

<!-- Page 1 : couverture -->
<section class="page p1">
  <div class="brand">velorancasa</div>
  <div class="photo hero" role="img" aria-label="Photo du grand balcon carrelé avec garde-corps, vue sur la verdure"></div>
  <div class="title-band">
    <div class="t1">LUMINEUX 4.5 DE 100M2 IDÉALEMENT SITUÉ !</div>
    <div class="t2">À 1200 GENÈVE</div>
    <div class="broker">Votre courtier &nbsp;|&nbsp; Claire Duvanel
      <svg viewBox="0 0 24 24" fill="#fff"><path d="M6.6 10.8a15.1 15.1 0 0 0 6.6 6.6l2.2-2.2c.3-.3.7-.4 1-.2 1.1.4 2.3.6 3.6.6.6 0 1 .4 1 1V20c0 .6-.4 1-1 1A17 17 0 0 1 3 4c0-.6.4-1 1-1h3.5c.6 0 1 .4 1 1 0 1.3.2 2.5.6 3.6.1.3 0 .7-.2 1z"/></svg>
      0791112233</div>
  </div>
  <div class="facts">
    <div class="facts-grid">
      <span>TYPE DE BIEN</span><span class="val">APPARTEMENT</span><span>PRIX</span><span class="val">895 000.-</span>
      <span>SURFACE HABITABLE M2</span><span class="val">100 M²</span><span>ANNÉE DE</span><span class="val">1994</span>
      <span>NOMBRE DE PIÈCES</span><span class="val">4.5</span><span>ETAT</span><span class="val">BON ÉTAT</span>
      <span>SURFACE PARCELLE M2</span><span class="val">0 M²</span><span>LIBRE DÈS LE</span><span class="val"></span>
    </div>
  </div>
  <footer class="footer">
    <div class="f-col f-company"><div class="name"><svg viewBox="0 0 24 24"><path d="M12 3 2 12h3v9h5v-6h4v6h5v-9h3z"/></svg>VELORANCASA SÀRL</div><div class="addr">Chemin du Verger 12, 1804 Corsier</div></div>
    <div class="f-col f-web"><div><svg viewBox="0 0 24 24"><path d="M2 5h20v14H2zm2 2v.5l8 5 8-5V7z"/></svg>INFO@VELORANCASA.CH</div><div><svg viewBox="0 0 24 24"><circle cx="12" cy="12" r="10"/></svg>WWW.VELORANCASA.CH</div></div>
    <div class="f-col f-phone"><div><svg viewBox="0 0 24 24"><path d="M6.6 10.8a15.1 15.1 0 0 0 6.6 6.6l2.2-2.2c.3-.3.7-.4 1-.2 1.1.4 2.3.6 3.6.6.6 0 1 .4 1 1V20c0 .6-.4 1-1 1A17 17 0 0 1 3 4c0-.6.4-1 1-1h3.5c.6 0 1 .4 1 1 0 1.3.2 2.5.6 3.6.1.3 0 .7-.2 1z"/></svg>021 555 40 12</div><div><svg viewBox="0 0 24 24"><path d="M4 8h16v12H4zM7 3h10v5H7z"/></svg>021 555 40 19</div></div>
  </footer>
</section>

<!-- Page 2 : description -->
<section class="page p2">
  <div class="brand">velorancasa</div>
  <div class="head-rule"></div>
  <h2 class="sec-title" style="top:76px">DESCRIPTION :</h2>
  <div class="desc">
    <p>Venez visiter sans tarder ce bel appartement situé dans un environnement calme et vert, proche du centre-ville et de toutes les commodités. Il offre de beaux volumes et des pièces de vie très lumineuses. Au 1er étage d'une copropriété soignée, c'est le bien idéal pour un couple ou une famille.</p>
    <p>Cet appartement pourrait aussi convenir comme investissement pour un client souhaitant le louer.</p>
    <p>Il est en bon état d'entretien et se réjouit d'accueillir ses nouveaux propriétaires !</p>
    <p>Il se distribue ainsi</p>
    <p>Une entrée avec armoire encastrée dessert de part et d'autre la partie jour et la partie nuit. La spacieuse pièce de vie se compose d'une cuisine ouverte entièrement équipée et aménagée s'ouvrant sur le séjour. Il profite d'une exposition optimale. Du séjour, vous avez accès à un agréable balcon qui offre une belle vue dégagée sur un environnement verdoyant.</p>
    <p>La partie nuit offre trois belles chambres, une salle de bains avec baignoire, lavabo, wc ainsi qu'un wc visiteurs.</p>
    <p>Deux places de parc intérieures en sus s'ajoutent à ce bel appartement. N'hésitez pas, contactez-moi pour plus d'informations et pour une visite !</p>
  </div>
  <div class="photo agent-photo" role="img" aria-label="Portrait de la courtière"></div>
  <div class="agent-name">Claire Duvanel</div>
  <div class="agent-phone"><svg viewBox="0 0 24 24"><path d="M6.6 10.8a15.1 15.1 0 0 0 6.6 6.6l2.2-2.2c.3-.3.7-.4 1-.2 1.1.4 2.3.6 3.6.6.6 0 1 .4 1 1V20c0 .6-.4 1-1 1A17 17 0 0 1 3 4c0-.6.4-1 1-1h3.5c.6 0 1 .4 1 1 0 1.3.2 2.5.6 3.6.1.3 0 .7-.2 1z"/></svg>0791112233</div>
  <h2 class="sec-title" style="top:266px">COMMODITÉS :</h2>
  <div class="comm-rule"></div>
  <div class="comm comm-left">
    <div><b>ETAGE :</b> 1er étage</div>
    <div><b>VUE :</b> vue dégagée sur le parc</div>
    <div><b>COMMERCES :</b> à proximité immédiate</div>
    <div><b>ECOLES :</b> Collège du Vallon</div>
    <div><b>TRANSPORTS PUBLICS :</b> à 5 minutes à pied</div>
  </div>
  <div class="comm comm-right">
    <div><b>CHAUFFAGE :</b> mazout / au sol</div>
    <div><b>CAVE :</b> oui</div>
    <div><b>GARAGE :</b> 2 places de parc intérieures</div>
    <div><b>BALCON :</b> oui</div>
    <div><b>ASCENSEUR :</b> oui</div>
  </div>
  <div class="photo interior" style="left:23px;top:374px;width:165px;height:127px" role="img" aria-label="Séjour lumineux avec parquet et baies vitrées"></div>
  <div class="photo kitchen" style="left:203px;top:374px;width:164px;height:127px" role="img" aria-label="Cuisine ouverte équipée"></div>
  <footer class="footer">
    <div class="f-col f-company"><div class="name"><svg viewBox="0 0 24 24"><path d="M12 3 2 12h3v9h5v-6h4v6h5v-9h3z"/></svg>VELORANCASA SÀRL</div><div class="addr">Chemin du Verger 12, 1804 Corsier</div></div>
    <div class="f-col f-web"><div><svg viewBox="0 0 24 24"><path d="M2 5h20v14H2zm2 2v.5l8 5 8-5V7z"/></svg>INFO@VELORANCASA.CH</div><div><svg viewBox="0 0 24 24"><circle cx="12" cy="12" r="10"/></svg>WWW.VELORANCASA.CH</div></div>
    <div class="f-col f-phone"><div><svg viewBox="0 0 24 24"><path d="M6.6 10.8a15.1 15.1 0 0 0 6.6 6.6l2.2-2.2c.3-.3.7-.4 1-.2 1.1.4 2.3.6 3.6.6.6 0 1 .4 1 1V20c0 .6-.4 1-1 1A17 17 0 0 1 3 4c0-.6.4-1 1-1h3.5c.6 0 1 .4 1 1 0 1.3.2 2.5.6 3.6.1.3 0 .7-.2 1z"/></svg>021 555 40 12</div><div><svg viewBox="0 0 24 24"><path d="M4 8h16v12H4zM7 3h10v5H7z"/></svg>021 555 40 19</div></div>
  </footer>
</section>

<!-- Page 3 : situation -->
<section class="page p3">
  <div class="brand">velorancasa</div>
  <div class="head-rule"></div>
  <h2 class="sec-title" style="top:76px">SITUATION</h2>
  <p class="situ">Cet appartement a l'avantage de se situer proche de toutes les commodités, à 3 minutes du Collège du Vallon, à 1 minute de l'arrêt de bus et à 3 minutes des axes autoroutiers. Vous rejoindrez le centre-ville en 7 minutes. Des atouts que vous saurez apprécier.</p>
  <div class="photo interior" style="left:23px;top:114px;width:165px;height:118px" role="img" aria-label="Séjour avec cuisine ouverte"></div>
  <div class="photo kitchen" style="left:203px;top:114px;width:164px;height:118px" role="img" aria-label="Hall d'entrée et cuisine"></div>
  <div class="photo interior" style="left:23px;top:248px;width:165px;height:118px" role="img" aria-label="Séjour avec accès au balcon"></div>
  <div class="photo kitchen" style="left:203px;top:248px;width:164px;height:118px" role="img" aria-label="Armoires encastrées de l'entrée"></div>
  <div class="photo interior" style="left:23px;top:382px;width:165px;height:119px" role="img" aria-label="Couloir de la partie nuit"></div>
  <div class="photo interior" style="left:203px;top:382px;width:164px;height:119px" role="img" aria-label="Chambre lumineuse avec parquet"></div>
  <footer class="footer">
    <div class="f-col f-company"><div class="name"><svg viewBox="0 0 24 24"><path d="M12 3 2 12h3v9h5v-6h4v6h5v-9h3z"/></svg>VELORANCASA SÀRL</div><div class="addr">Chemin du Verger 12, 1804 Corsier</div></div>
    <div class="f-col f-web"><div><svg viewBox="0 0 24 24"><path d="M2 5h20v14H2zm2 2v.5l8 5 8-5V7z"/></svg>INFO@VELORANCASA.CH</div><div><svg viewBox="0 0 24 24"><circle cx="12" cy="12" r="10"/></svg>WWW.VELORANCASA.CH</div></div>
    <div class="f-col f-phone"><div><svg viewBox="0 0 24 24"><path d="M6.6 10.8a15.1 15.1 0 0 0 6.6 6.6l2.2-2.2c.3-.3.7-.4 1-.2 1.1.4 2.3.6 3.6.6.6 0 1 .4 1 1V20c0 .6-.4 1-1 1A17 17 0 0 1 3 4c0-.6.4-1 1-1h3.5c.6 0 1 .4 1 1 0 1.3.2 2.5.6 3.6.1.3 0 .7-.2 1z"/></svg>021 555 40 12</div><div><svg viewBox="0 0 24 24"><path d="M4 8h16v12H4zM7 3h10v5H7z"/></svg>021 555 40 19</div></div>
  </footer>
</section>

<!-- Page 4 : galerie -->
<section class="page p4">
  <div class="brand">velorancasa</div>
  <div class="head-rule"></div>
  <div class="photo kitchen" style="left:23px;top:80px;width:165px;height:125px" role="img" aria-label="Entrée avec armoires et vue sur la cuisine"></div>
  <div class="photo wardrobe" style="left:203px;top:80px;width:164px;height:125px" role="img" aria-label="Chambre avec grande armoire sombre"></div>
  <div class="photo interior" style="left:23px;top:229px;width:165px;height:125px" role="img" aria-label="Chambre avec fenêtre et parquet"></div>
  <div class="photo interior" style="left:203px;top:229px;width:164px;height:125px" role="img" aria-label="Chambre lumineuse"></div>
  <div class="photo bath" style="left:23px;top:374px;width:165px;height:127px" role="img" aria-label="Salle de bains avec lavabo, wc et baignoire"></div>
  <div class="photo garden" style="left:203px;top:374px;width:164px;height:127px" role="img" aria-label="Jardin arboré de la résidence"></div>
  <footer class="footer">
    <div class="f-col f-company"><div class="name"><svg viewBox="0 0 24 24"><path d="M12 3 2 12h3v9h5v-6h4v6h5v-9h3z"/></svg>VELORANCASA SÀRL</div><div class="addr">Chemin du Verger 12, 1804 Corsier</div></div>
    <div class="f-col f-web"><div><svg viewBox="0 0 24 24"><path d="M2 5h20v14H2zm2 2v.5l8 5 8-5V7z"/></svg>INFO@VELORANCASA.CH</div><div><svg viewBox="0 0 24 24"><circle cx="12" cy="12" r="10"/></svg>WWW.VELORANCASA.CH</div></div>
    <div class="f-col f-phone"><div><svg viewBox="0 0 24 24"><path d="M6.6 10.8a15.1 15.1 0 0 0 6.6 6.6l2.2-2.2c.3-.3.7-.4 1-.2 1.1.4 2.3.6 3.6.6.6 0 1 .4 1 1V20c0 .6-.4 1-1 1A17 17 0 0 1 3 4c0-.6.4-1 1-1h3.5c.6 0 1 .4 1 1 0 1.3.2 2.5.6 3.6.1.3 0 .7-.2 1z"/></svg>021 555 40 12</div><div><svg viewBox="0 0 24 24"><path d="M4 8h16v12H4zM7 3h10v5H7z"/></svg>021 555 40 19</div></div>
  </footer>
</section>

</body>
</html>
```